New banner graphics for Kelbro.com website

I've developed a software tool that helps businesses ensure they are working on their most valuable and important work.

I would like a banner graphic for my home page (www.kelbro.com) that can somehow capture the value of focus and intentional outcomes.

I had an initial thought of a starry sky that shifts focus to a few bright stars, but while that might sound ok, I think my idea is lame hence I'm coming to you guys.

My sites two primary colors are a soft purple and gray.
#919EC1(purple)
#9E9E9E (gray)

Target Market(s)

B2B for enterprises. Typical customers are CFOs, CIOs/Heads of IT

Industry/Entity Type

Business Software

Number of Pages Required

1 page

Font styles to use
Sans Serif

Colors
b8a6cd
cedeed

Requirements
Must have
• I use Divi as my Wordpress theme and the current main landing page can be seen at www.kelbro.com.
• My logo colors are:
• #919EC1(purple)
• #9E9E9E (gray)
Should not have
• Lots of distraction or visual "noise". I want to re-enforce the message that my software is focused on their business and not my products or website.

```html
<!DOCTYPE html>
<html lang="en">
<head>
<meta charset="utf-8">
<title>Kelbro – Home Banner</title>
<link href="https://fonts.googleapis.com/css2?family=Open+Sans:wght@400;600;700&display=swap" rel="stylesheet">
<style>
  :root {
    --stage: #4f4f4f;
    --brand-purple: #919ec1;
    --band-deep: #7f8bb1;
    --brand-gray: #9e9e9e;
    --headline-blue: #2f4fa6;
    --ink: #222222;
    --white: #ffffff;
    --panel-light: #f4f4f5;
    --panel-mid: #e4e4e6;
  }
  html, body {
    margin: 0;
    width: 1200px;
    height: 1200px;
    overflow: hidden;
    background: var(--stage);
  }
  .banner {
    position: absolute;
    left: 40px;
    top: 344px;
    width: 1120px;
    height: 511px;
    display: block;
    font-family: "Open Sans", sans-serif;
  }
  .brand-name { font-size: 74px; font-weight: 400; fill: var(--brand-gray); }
  .headline { font-size: 64px; font-weight: 700; fill: var(--headline-blue); }
  .tagline { font-size: 27px; font-weight: 600; fill: var(--ink); }
  .site-url { font-size: 22px; font-weight: 700; fill: var(--white); letter-spacing: 6px; }
  .benefit { font-size: 19px; font-weight: 600; fill: var(--white); }
  .benefit-dot { fill: #4a4a4a; }
</style>
</head>
<body>
<svg class="banner" viewBox="0 0 1080 493" xmlns="http://www.w3.org/2000/svg">
  <defs>
    <linearGradient id="leftPanel" x1="0" y1="0" x2="0" y2="1">
      <stop offset="0" stop-color="#ececee"/>
      <stop offset="0.5" stop-color="#ffffff"/>
    </linearGradient>
    <linearGradient id="rightPanel" x1="0" y1="0" x2="1" y2="0">
      <stop offset="0" stop-color="var(--white)"/>
      <stop offset="1" stop-color="var(--panel-mid)"/>
    </linearGradient>
    <linearGradient id="band" x1="0" y1="0" x2="0" y2="1">
      <stop offset="0" stop-color="var(--band-deep)"/>
      <stop offset="1" stop-color="var(--brand-purple)"/>
    </linearGradient>
    <linearGradient id="rule" x1="0" y1="0" x2="1" y2="0">
      <stop offset="0" stop-color="#bbbbbb" stop-opacity="0"/>
      <stop offset="0.5" stop-color="#9a9a9a"/>
      <stop offset="1" stop-color="#bbbbbb" stop-opacity="0"/>
    </linearGradient>
    <linearGradient id="photoTeam" x1="0" y1="0" x2="1" y2="1">
      <stop offset="0" stop-color="#e9eef3"/>
      <stop offset="1" stop-color="#3a4f73"/>
    </linearGradient>
    <linearGradient id="photoMeeting" x1="0" y1="0" x2="1" y2="1">
      <stop offset="0" stop-color="#f2f4f5"/>
      <stop offset="1" stop-color="#8b8f98"/>
    </linearGradient>
  </defs>

  <!-- base panel -->
  <rect class="base-panel" width="1080" height="493" fill="url(#leftPanel)"/>

  <!-- right message panel with gray swoop rim -->
  <path class="message-panel" d="M505,0 C455,40 470,100 505,160 C540,220 530,270 540,285 C600,330 700,345 820,320 C920,300 1000,285 1080,290 L1080,0 Z" fill="url(#rightPanel)"/>
  <path class="swoop-rim" d="M505,0 C455,40 470,100 505,160 C540,220 530,270 540,285 C600,330 700,345 820,320 C920,300 1000,285 1080,290" fill="none" stroke="var(--brand-gray)" stroke-width="10"/>

  <!-- purple bottom band -->
  <path class="purple-band" d="M0,375 C120,320 400,360 480,330 C515,315 530,300 540,292 C600,345 700,358 820,333 C920,313 1000,302 1080,305 L1080,470 L0,470 Z" fill="url(#band)"/>
  <path class="band-edge" d="M548,296 C610,340 700,352 820,328 C920,308 1000,298 1080,300" fill="none" stroke="var(--white)" stroke-width="5"/>
  <rect class="footer-strip" x="0" y="470" width="1080" height="23" fill="#ededee"/>

  <!-- brand name -->
  <text class="brand-name" x="78" y="105">kelbro</text>

  <!-- photo circles -->
  <circle cx="145" cy="290" r="96" fill="#e2e2e3"/>
  <circle cx="145" cy="290" r="88" fill="url(#photoTeam)" role="img" aria-label="Photo: business team giving thumbs up around a laptop"/>
  <circle cx="342" cy="282" r="114" fill="#e2e2e3"/>
  <circle cx="342" cy="282" r="104" fill="url(#photoMeeting)" role="img" aria-label="Photo: team meeting at a table with a bar chart presentation"/>

  <!-- headline -->
  <text class="headline" x="1022" y="118" text-anchor="end">Get FOCUSPLAN</text>
  <rect class="headline-rule" x="540" y="137" width="480" height="2" fill="url(#rule)"/>
  <text class="tagline" x="1019" y="194" text-anchor="end">A simple software tool that makes</text>
  <text class="tagline" x="1019" y="231" text-anchor="end">your business goals actionable</text>

  <!-- url -->
  <text class="site-url" x="245" y="442" text-anchor="middle">www.kelbro.com</text>

  <!-- benefits -->
  <g class="benefits">
    <text class="benefit" x="624" y="409" text-anchor="end">Define the Outcomes</text>
    <circle class="benefit-dot" cx="640" cy="403" r="6"/>
    <text class="benefit" x="624" y="434" text-anchor="end">Set the Direction</text>
    <circle class="benefit-dot" cx="640" cy="428" r="6"/>

    <text class="benefit" x="852" y="409" text-anchor="end">Focus the Resources</text>
    <circle class="benefit-dot" cx="868" cy="403" r="6"/>
    <text class="benefit" x="852" y="434" text-anchor="end">Reduce the Risk</text>
    <circle class="benefit-dot" cx="868" cy="428" r="6"/>

    <text class="benefit" x="1033" y="409" text-anchor="end">Increase Team</text>
    <circle class="benefit-dot" cx="1046" cy="403" r="6"/>
    <text class="benefit" x="1033" y="434" text-anchor="end">Engagement</text>
  </g>
</svg>
</body>
</html>
```